1200 x 150 pixel banner ad max size 200KB

Hi - I'm looking for an animated GIF to be used as an online digital banner advert.

The banner ad is to promote sales of gas cylinders from a world-leading manufacturer.

Headline 1: SLASH YOUR ADMINISTRATION COSTS BY 50%
Headline 2: If you're not happy with our service - we will give you your money back!
Headline 3 (if possible): FREE Regulator for all new customers/vessels

**The banner needs to really stand out of the page and reflect our company and brand - We exist to revolutionise ship safety, performance and crew welfare.**

The banner ad needs to include the product logo and company logo - both attached.

The blue colours in our logos are:
Dark Blue
Pantone 303
C100 M047 Y023 K079
R000 G031 B051
HTML 001F33

Light Blue
Pantone 2995
CO83 M001 Y000 K000
R080 G177 B234
HTML 05B1EA

Target Market(s)

Marine industry buyers - fleet managers, ship owners, technical purchasers, superintendants

Industry/Entity Type

Marine

Requirements
Must have
• Company colours, product and company logo

```html
<!DOCTYPE html>
<html lang="en">
<head>
<meta charset="utf-8">
<title>HarbourLine Gas – Banner Set</title>
<link rel="stylesheet" href="https://fonts.googleapis.com/css2?family=Arimo:wght@400;700&display=swap">
<style>
  :root {
    --stage: #e4e4e4;
    --paper: #ffffff;
    --brand-light: #1ba9df;
    --brand-dark: #1a2a3a;
    --headline: #ffffff;
    --frame-line: #2a9fd2;
  }
  * { box-sizing: border-box; margin: 0; padding: 0; }
  html, body { width: 1200px; height: 850px; overflow: hidden; }
  body {
    background: var(--stage);
    font-family: "Arimo", Arial, sans-serif;
    position: relative;
  }
  .banner {
    position: absolute;
    left: 46px;
    width: 1106px;
    height: 138px;
    background: var(--paper);
    overflow: hidden;
  }
  .banner--admin { top: 187px; }
  .banner--refund { top: 358px; }
  .banner--regulator { top: 526px; }
  .banner__sweep { position: absolute; inset: 0; width: 100%; height: 100%; }
  .banner__sweep path { fill: var(--brand-light); }
  .brand {
    position: absolute;
    left: 40px;
    top: 0;
    height: 138px;
    display: flex;
    align-items: center;
    gap: 14px;
  }
  .brand__mark {
    width: 34px; height: 34px;
    background: var(--brand-dark);
    flex: none;
  }
  .brand__name {
    font-weight: 700;
    font-size: 33px;
    color: var(--brand-dark);
    letter-spacing: -0.5px;
    line-height: 1;
  }
  .headline {
    position: absolute;
    color: var(--headline);
    font-weight: 700;
  }
  .banner--admin .headline {
    left: 581px; width: 440px; top: 29px;
    text-align: center; font-size: 31px; line-height: 40px;
  }
  .banner--refund .headline {
    left: 598px; width: 440px; top: 30px;
    text-align: left; font-size: 26px; line-height: 35px; letter-spacing: 0.3px;
  }
  .banner--regulator .headline {
    left: 579px; width: 470px; top: 22px; height: 88px;
    text-align: center; font-size: 30px; line-height: 39px;
    border: 1px solid var(--frame-line);
  }
</style>
</head>
<body>
  <section class="banner banner--admin">
    <svg class="banner__sweep" viewBox="0 0 1106 138" preserveAspectRatio="none" aria-hidden="true">
      <path d="M304 138 Q430 40 648 0 L1106 0 L1106 138 Z"/>
    </svg>
    <div class="brand">
      <span class="brand__mark"></span>
      <span class="brand__name">HarbourLine Gas</span>
    </div>
    <p class="headline">Slash Your Administration Costs By 50%</p>
  </section>

  <section class="banner banner--refund">
    <svg class="banner__sweep" viewBox="0 0 1106 138" preserveAspectRatio="none" aria-hidden="true">
      <path d="M280 138 Q410 40 622 0 L1106 0 L1106 138 Z"/>
    </svg>
    <div class="brand">
      <span class="brand__mark"></span>
      <span class="brand__name">HarbourLine Gas</span>
    </div>
    <p class="headline">if you’re not happy with our service we will give you your money back</p>
  </section>

  <section class="banner banner--regulator">
    <svg class="banner__sweep" viewBox="0 0 1106 138" preserveAspectRatio="none" aria-hidden="true">
      <path d="M304 138 Q430 40 648 0 L1106 0 L1106 138 Z"/>
    </svg>
    <div class="brand">
      <span class="brand__mark"></span>
      <span class="brand__name">HarbourLine Gas</span>
    </div>
    <p class="headline">FREE Regulator for all new customers/vessels</p>
  </section>
</body>
</html>
```